Copper Ridge Resort & Marina - Boat Slips, Cabin Rentals, Floating Vacation Homes, & More

We need an 8'H x 16'W billboard for our Resort & marina, www.copperridgeresort.example. We'd like it to include: Lakefront Cabin Rentals, Floating Vacation Homes, and New Slips Summer 2022. We'd like it to be simple using the colors on our logo, similar to our business cards, and have our logo on it large. Maybe an arrow on the bottom pointing left that says 3 miles, possibly our website and phone number.

Target Market(s)

Lake People, Boaters

Industry/Entity Type

Resort & Marina (Recreation/Hospitality)

Font styles to use
Sans Serif
Other font styles liked:
• Simple/modern

Colors
0054AA
0677BA
7BADD7
CADEEF
E8F1F8
FFC000
F8CF3A
FAE287
FDF2CF
FEFAEE
F0912C
F2A743
F7CA91
FBE8D2
FDF5EE

Requirements
Must have
• Logo, Cabin Rentals, Floating Vacation Homes, New Slips Summer 2022
Nice to have
• An additional banner hanging from the bottom with an orange (or blue, colors from our logo) arrow pointing left, with white text saying: 3 miles 555-214-0867 www.copperridgeresort.example
Should not have
• Shouldn't be too busy

```html
<!DOCTYPE html>
<html lang="en">
<head>
<meta charset="utf-8">
<title>Copper Ridge Resort &amp; Marina – Billboard</title>
<link rel="stylesheet" href="https://fonts.googleapis.com/css2?family=Playfair+Display:wght@500;700&family=Montserrat:wght@700;800&display=swap">
<style>
  :root{
    --blue-deep:#0054AA;
    --blue-mid:#0677BA;
    --blue-sky:#7BADD7;
    --navy:#1D4E8F;
    --yellow:#FFC000;
    --yellow-soft:#F8CF3A;
    --orange:#F0912C;
    --white:#FFFFFF;
    --page:#FFFFFF;
  }
  *{margin:0;padding:0;box-sizing:border-box}
  html,body{width:960px;height:1200px;overflow:hidden;background:var(--page)}
  .canvas{position:relative;width:960px;height:1200px}
  .billboard{
    position:absolute;left:30px;top:420px;width:900px;height:359px;
    background:var(--white);overflow:hidden;
    box-shadow:0 6px 22px rgba(0,0,0,.35);
  }
  .billboard__waves{position:absolute;inset:0;width:100%;height:100%}
  .brand{
    position:absolute;left:560px;top:60px;width:310px;
    display:flex;align-items:center;gap:12px;
    font-family:"Playfair Display",Georgia,serif;font-weight:500;color:var(--navy);
  }
  .brand__dot{width:30px;height:30px;border-radius:50%;background:var(--orange);flex:none}
  .brand__name{font-size:27px;line-height:1.05;letter-spacing:.5px}
  .brand__name small{display:block;font-size:15px;letter-spacing:2px}
  .offers{
    position:absolute;left:70px;top:100px;list-style:none;
    font-family:"Playfair Display",Georgia,serif;font-weight:700;color:var(--white);
    font-size:41px;line-height:53px;
  }
  .lake-map{
    position:absolute;left:640px;top:160px;width:135px;height:112px;border-radius:6px;
    background:linear-gradient(160deg,rgba(255,255,255,.85),rgba(232,241,248,.6));
  }
  .lake-label{
    position:absolute;left:730px;top:262px;
    font-family:"Playfair Display",Georgia,serif;font-weight:700;color:var(--white);font-size:19px;
  }
  .distance{position:absolute;left:51px;top:273px;display:flex;align-items:center;height:62px}
  .distance__arrow{width:58px;height:62px;flex:none}
  .distance__text{
    font-family:"Montserrat",Arial,sans-serif;font-weight:800;color:var(--yellow);
    font-size:31px;margin-left:8px;letter-spacing:.5px;
  }
  .distance__flag{width:46px;height:36px;margin-left:7px;flex:none}
  .contact{
    position:absolute;left:338px;top:298px;display:flex;gap:22px;align-items:center;
    font-family:"Montserrat",Arial,sans-serif;font-weight:700;color:var(--yellow);font-size:19px;
  }
  .contact__item{display:flex;align-items:center;gap:6px}
  .contact__icon{width:17px;height:17px}
</style>
</head>
<body>
<main class="canvas">
  <section class="billboard" aria-label="Copper Ridge Resort and Marina billboard">
    <svg class="billboard__waves" viewBox="0 0 1385 552" preserveAspectRatio="none" aria-hidden="true">
      <path fill="var(--orange)" d="M0,155 C160,40 330,15 500,45 C680,80 860,235 1060,250 C1190,262 1300,235 1385,185 L1385,552 L0,552 Z"/>
      <path fill="var(--yellow)" d="M0,195 C165,70 335,45 500,62 C680,95 860,258 1060,275 C1190,285 1300,262 1385,235 L1385,552 L0,552 Z"/>
      <defs>
        <linearGradient id="blueFill" x1="0" y1="0" x2="0" y2="1">
          <stop offset="0" stop-color="var(--blue-deep)"/>
          <stop offset="1" stop-color="#0A5FB2"/>
        </linearGradient>
      </defs>
      <path fill="url(#blueFill)" d="M0,235 C170,100 340,65 500,75 C680,105 860,275 1060,288 C1190,296 1300,282 1385,243 L1385,552 L0,552 Z"/>
    </svg>

    <div class="brand">
      <span class="brand__dot"></span>
      <p class="brand__name">Copper Ridge<small>Resort &amp; Marina</small></p>
    </div>

    <ul class="offers">
      <li>Cabin Rentals</li>
      <li>Floating Vacation Homes</li>
      <li>New Slips Summer 2022</li>
    </ul>

    <div class="lake-map" role="img" aria-label="White outline map of the lake"></div>
    <p class="lake-label">Lake Texoma</p>

    <div class="distance">
      <svg class="distance__arrow" viewBox="0 0 58 62" aria-hidden="true">
        <path fill="var(--yellow)" d="M0,31 L37,0 L37,16 L58,16 L58,46 L37,46 L37,62 Z"/>
      </svg>
      <span class="distance__text">3 MILES</span>
      <svg class="distance__flag" viewBox="0 0 46 36" aria-hidden="true">
        <path fill="var(--yellow)" d="M0,0 L46,0 L34,18 L46,36 L0,36 Z"/>
      </svg>
    </div>

    <div class="contact">
      <span class="contact__item">
        <svg class="contact__icon" viewBox="0 0 24 24" aria-hidden="true">
          <circle cx="12" cy="12" r="10.5" fill="none" stroke="var(--white)" stroke-width="1.6"/>
          <path fill="var(--white)" d="M8.6,6.5 L10.2,6.3 L11.1,9 L10,10 C10.6,11.5 11.9,12.9 13.6,13.7 L14.6,12.6 L17.3,13.5 L17.1,15.2 C16.8,16.3 15.6,16.8 14.5,16.5 C10.8,15.4 8.2,12.8 7.3,9.3 C7,8 7.6,6.8 8.6,6.5 Z"/>
        </svg>
        555-214-0867
      </span>
      <span class="contact__item">
        <svg class="contact__icon" viewBox="0 0 24 24" aria-hidden="true" fill="none" stroke="var(--white)" stroke-width="1.6">
          <circle cx="12" cy="12" r="10.5"/>
          <ellipse cx="12" cy="12" rx="4.5" ry="10.5"/>
          <path d="M1.5,12 H22.5 M3.5,6.5 H20.5 M3.5,17.5 H20.5"/>
        </svg>
        www.copperridgeresort.example
      </span>
    </div>
  </section>
</main>
</body>
</html>
```